Applied environmental services company startup chasing a look

Small team of practical, technical and management-focused people in a business that can write the report, do the work written up in the report cost effectively. Vertical integration from design through to application. This business will be chasing opportunities where project management melds with technical application for clients needing forestry, environmental or natural resource management work done. We need a graphic and style for use in Microsoft Word and Powerpoint. A template including fonts, headings and styles would be great. Don't have a name yet, however I do like Tallbrook Equity, Tallbrook Merit, Tallbrook Holdings...

Industry/Entity Type

It Company

Requirements
Nice to have
• I would like different shades of blue to be a part of the design.

```html
<!DOCTYPE html>
<html lang="en">
<head>
<meta charset="utf-8">
<title>Tallbrook Equity – Presentation Template</title>
<link href="https://fonts.googleapis.com/css2?family=Open+Sans:wght@400;600;700&display=swap" rel="stylesheet">
<style>
  :root {
    --stage: #d9d9d9;
    --navy: #0a4f7e;
    --blue-deep: #0a6aa8;
    --blue: #1590cc;
    --cyan: #27b6e0;
    --sky: #7fd3f0;
    --ice: #eaf6fb;
    --white: #ffffff;
    --grey-text: #5a6670;
    --ink: #2a2f35;
  }
  * { margin: 0; padding: 0; box-sizing: border-box; }
  html, body { width: 1200px; height: 960px; overflow: hidden; }
  body {
    background: var(--stage);
    font-family: "Open Sans", Arial, sans-serif;
    position: relative;
  }
  .slide {
    position: absolute;
    width: 463px;
    height: 342px;
    overflow: hidden;
    box-shadow: 0 6px 14px rgba(0,0,0,0.25);
  }
  .slide--cover { left: 89px; top: 76px; }
  .slide--content-a { left: 629px; top: 76px; }
  .slide--content-b { left: 89px; top: 496px; }
  .slide--closing { left: 629px; top: 496px; }

  .slide svg.backdrop { position: absolute; inset: 0; }

  /* brand lockup */
  .brand { position: absolute; display: flex; align-items: center; gap: 8px; }
  .brand__text { display: flex; flex-direction: column; align-items: flex-end; }
  .brand__name {
    font-weight: 700; color: var(--navy); letter-spacing: -0.3px; line-height: 1;
  }
  .brand__tag { color: var(--grey-text); line-height: 1.1; }
  .brand__dot { border-radius: 50%; background: var(--blue); flex: none; }

  .brand--large .brand__name { font-size: 20px; }
  .brand--large .brand__tag { font-size: 10px; }
  .brand--large .brand__dot { width: 30px; height: 30px; }
  .brand--small .brand__name { font-size: 13px; }
  .brand--small .brand__tag { font-size: 7px; }
  .brand--small .brand__dot { width: 22px; height: 22px; }

  /* cover */
  .cover__title {
    position: absolute; left: 34px; top: 68px;
    color: var(--white); font-size: 24px; font-weight: 400; letter-spacing: 0.3px;
  }
  .cover__subtitle {
    position: absolute; left: 35px; top: 100px;
    color: var(--white); font-size: 14px; font-weight: 400;
  }
  .web {
    position: absolute; color: var(--white); font-size: 9px; opacity: 0.9;
  }
  .web b { font-weight: 700; }

  /* content slides */
  .slide--content { background: var(--white); }
  .header-mark {
    position: absolute; left: 0; top: 36px; width: 14px; height: 14px; background: var(--blue);
  }
  .heading {
    position: absolute; left: 30px; top: 34px;
    font-size: 15px; color: var(--ink); font-weight: 400;
  }
  .heading span { color: var(--blue); }
  .footer-bar {
    position: absolute; left: 0; bottom: 0; width: 100%; height: 22px;
    background: linear-gradient(90deg, var(--blue) 0%, var(--cyan) 45%, var(--blue-deep) 100%);
  }
  .footer-date {
    position: absolute; left: 36px; bottom: 5px; color: var(--white); font-size: 9px;
  }

  /* closing */
  .closing__title {
    position: absolute; left: 0; width: 100%; top: 82px; text-align: center;
    color: var(--white); font-size: 28px; font-weight: 400; letter-spacing: 0.4px;
  }
  .closing__subtitle {
    position: absolute; left: 0; width: 100%; top: 121px; text-align: center;
    color: var(--white); font-size: 15px; font-weight: 400;
  }
  .contact-row {
    position: absolute; left: 84px; top: 284px; display: flex; gap: 8px;
  }
  .contact {
    width: 68px; color: var(--white); font-size: 5.5px; font-weight: 700; line-height: 1.3;
  }
  .contact svg { display: block; margin: 0 0 8px 0; }
  .contact__bar {
    margin-top: 3px; height: 6px; background: rgba(255,255,255,0.35);
  }
</style>
</head>
<body>

  <!-- Cover slide -->
  <section class="slide slide--cover">
    <svg class="backdrop" width="463" height="342" viewBox="0 0 463 342">
      <defs>
        <linearGradient id="coverSky" x1="0" y1="0" x2="1" y2="1">
          <stop offset="0" stop-color="#2aa6de"/>
          <stop offset="1" stop-color="#0f83c4"/>
        </linearGradient>
        <linearGradient id="coverBand" x1="0" y1="0" x2="1" y2="0">
          <stop offset="0" stop-color="#ffffff"/>
          <stop offset="0.6" stop-color="#f4fbfe"/>
          <stop offset="1" stop-color="#cdeefa"/>
        </linearGradient>
        <linearGradient id="coverBase" x1="0" y1="0" x2="0" y2="1">
          <stop offset="0" stop-color="#1a98d2"/>
          <stop offset="1" stop-color="#0c6fae"/>
        </linearGradient>
      </defs>
      <rect width="463" height="188" fill="url(#coverSky)"/>
      <path d="M0 188 C150 170 300 120 463 95 L463 188 Z" fill="#7fd3f0" opacity="0.35"/>
      <path d="M120 188 C260 160 360 130 463 110" stroke="#ffffff" stroke-width="2" fill="none" opacity="0.6"/>
      <path d="M200 188 C300 165 380 145 463 135" stroke="#ffffff" stroke-width="6" fill="none" opacity="0.35"/>
      <rect y="188" width="463" height="80" fill="url(#coverBand)"/>
      <rect y="268" width="463" height="74" fill="url(#coverBase)"/>
      <rect y="268" width="463" height="6" fill="#0a6aa8" opacity="0.5"/>
    </svg>
    <h1 class="cover__title">TITLES GOES HERE</h1>
    <p class="cover__subtitle">SUBTITLES GOES HERE</p>
    <div class="brand brand--large" style="left:34px; top:212px;">
      <div class="brand__text">
        <span class="brand__name">TALLBROOK EQUITY</span>
        <span class="brand__tag">Management Team</span>
      </div>
      <span class="brand__dot"></span>
    </div>
    <p class="web" style="left:36px; bottom:11px;">www.<b>tallbrookequity</b>.com</p>
  </section>

  <!-- Content slide A -->
  <section class="slide slide--content slide--content-a">
    <svg class="backdrop" width="463" height="342" viewBox="0 0 463 342">
      <path d="M0 250 C150 200 300 230 463 150" stroke="#eef4f7" stroke-width="30" fill="none"/>
    </svg>
    <span class="header-mark"></span>
    <h2 class="heading">Sharp <span>CHARTS</span></h2>
    <div class="brand brand--small" style="right:26px; top:32px;">
      <div class="brand__text">
        <span class="brand__name">TALLBROOK EQUITY</span>
        <span class="brand__tag">Management Team</span>
      </div>
      <span class="brand__dot"></span>
    </div>
    <div class="footer-bar"></div>
    <p class="footer-date">30.10.2013</p>
    <p class="web" style="right:28px; bottom:5px;">www.<b>tallbrookequity</b>.com</p>
  </section>

  <!-- Content slide B -->
  <section class="slide slide--content slide--content-b">
    <svg class="backdrop" width="463" height="342" viewBox="0 0 463 342">
      <path d="M0 250 C150 200 300 230 463 150" stroke="#eef4f7" stroke-width="30" fill="none"/>
    </svg>
    <span class="header-mark"></span>
    <h2 class="heading">Sharp <span>CHARTS</span></h2>
    <div class="brand brand--small" style="right:26px; top:32px;">
      <div class="brand__text">
        <span class="brand__name">TALLBROOK EQUITY</span>
        <span class="brand__tag">Management Team</span>
      </div>
      <span class="brand__dot"></span>
    </div>
    <div class="footer-bar"></div>
    <p class="footer-date">30.10.2013</p>
    <p class="web" style="right:28px; bottom:5px;">www.<b>tallbrookequity</b>.com</p>
  </section>

  <!-- Closing slide -->
  <section class="slide slide--closing">
    <svg class="backdrop" width="463" height="342" viewBox="0 0 463 342">
      <defs>
        <linearGradient id="closingSky" x1="0" y1="0" x2="1" y2="0">
          <stop offset="0" stop-color="#27b6e0"/>
          <stop offset="1" stop-color="#0b64a6"/>
        </linearGradient>
        <linearGradient id="closingBand" x1="0" y1="0" x2="1" y2="0">
          <stop offset="0" stop-color="#ffffff"/>
          <stop offset="0.7" stop-color="#f6fcfe"/>
          <stop offset="1" stop-color="#c9e8f6"/>
        </linearGradient>
        <linearGradient id="closingBase" x1="0" y1="0" x2="1" y2="0">
          <stop offset="0" stop-color="#2fc2e8"/>
          <stop offset="1" stop-color="#1691cf"/>
        </linearGradient>
      </defs>
      <rect width="463" height="202" fill="url(#closingSky)"/>
      <path d="M0 40 C120 0 300 10 463 110" stroke="#ffffff" stroke-width="3" stroke-dasharray="8 8" fill="none" opacity="0.3"/>
      <path d="M0 202 C150 170 320 150 463 170 L463 202 Z" fill="#0a5f98" opacity="0.35"/>
      <rect y="202" width="463" height="60" fill="url(#closingBand)"/>
      <rect y="262" width="463" height="80" fill="url(#closingBase)"/>
    </svg>
    <h2 class="closing__title">THANK YOU VERY MUCH</h2>
    <p class="closing__subtitle">FOR YOUR VALUEABLE TIME</p>
    <div class="brand brand--large" style="left:124px; top:216px;">
      <div class="brand__text">
        <span class="brand__name">TALLBROOK EQUITY</span>
        <span class="brand__tag">Management Team</span>
      </div>
      <span class="brand__dot"></span>
    </div>
    <div class="contact-row">
      <div class="contact">
        <svg width="14" height="12" viewBox="0 0 14 12"><path d="M7 0 L14 6 H12 V12 H8.5 V8 H5.5 V12 H2 V6 H0 Z" fill="#fff"/></svg>
        4470 CEDAR RIDGE<br>ALDEN, VA 20145
        <div class="contact__bar"></div>
      </div>
      <div class="contact">
        <svg width="12" height="12" viewBox="0 0 12 12"><rect x="1" y="0" width="10" height="12" rx="1.5" fill="#fff"/><rect x="3" y="2" width="6" height="3" fill="#1a98d2"/></svg>
        TEL: +1.555.014.2290
        <div class="contact__bar"></div>
      </div>
      <div class="contact">
        <svg width="14" height="10" viewBox="0 0 14 10"><rect width="14" height="10" fill="#fff"/><path d="M0 0 L7 6 L14 0" stroke="#1a98d2" fill="none"/></svg>
        TEL: +1.555.014.2290
        <div class="contact__bar"></div>
      </div>
      <div class="contact">
        <svg width="12" height="12" viewBox="0 0 12 12"><circle cx="6" cy="6" r="5.5" fill="#fff"/><ellipse cx="6" cy="6" rx="2.4" ry="5.5" stroke="#1a98d2" fill="none"/><path d="M0.5 6 H11.5" stroke="#1a98d2"/></svg>
        TEL: +1.555.014.2290
        <div class="contact__bar"></div>
      </div>
    </div>
  </section>

</body>
</html>
```